Brightpath Strategic Advisers F.Z.E
Professional
Khalid Yousef Nasser
Founder & CEO
Corvana Trade Park
info@bsa-qx.com
www.bsa-qx.com
Training & Consultancy on:
QBXR Assessment & Training
Leadership Development & Coaching
Change Management
Strategy Management
Performance Management
Quality & Process Management
TQM
HR Development
HR Procedures & Regulation
Logo & Full Stationeries & P.P Presentation first page and continues sheet & Proposal document cover & continues sheet

```html
<!DOCTYPE html>
<html lang="en">
<head>
<meta charset="utf-8">
<title>Brightpath Strategic Advisers – Business Cards</title>
<link rel="stylesheet" href="https://fonts.googleapis.com/css2?family=Open+Sans:ital,wght@0,400;0,600;0,700;1,400&family=Marcellus+SC&display=swap">
<style>
  :root {
    --bg: #e9e3da;
    --card-light: #ffffff;
    --card-dark: #2a2a2a;
    --orange: #f28a1e;
    --grey: #8d8d8d;
    --grey-light: #cfcfcf;
    --ink: #3a3a3a;
    --ink-light: #e8e8e8;
    --label: #3b3b3b;
  }
  * { box-sizing: border-box; margin: 0; padding: 0; }
  html, body { width: 1200px; height: 794px; overflow: hidden; }
  body { background: var(--bg); font-family: "Open Sans", Arial, sans-serif; position: relative; }

  .card {
    position: absolute; width: 500px; height: 281px;
    border-radius: 16px; overflow: hidden;
    box-shadow: 0 3px 8px rgba(0,0,0,.25);
  }
  .card--light { background: var(--card-light); color: var(--ink); }
  .card--dark { background: var(--card-dark); color: var(--ink-light); }
  .front-a { left: 72px; top: 38px; }
  .front-b { left: 629px; top: 38px; }
  .back-a { left: 72px; top: 415px; }
  .back-b { left: 629px; top: 415px; }

  .edge { position: absolute; inset: 0; width: 100%; height: 100%; }

  .brand {
    position: absolute; left: 26px; top: 110px; width: 220px;
    display: flex; align-items: center; gap: 8px;
  }
  .brand__dot { width: 14px; height: 14px; background: var(--orange); flex: none; }
  .brand__name { font-size: 13px; font-weight: 600; line-height: 1.2; letter-spacing: .2px; }

  .divider { position: absolute; left: 256px; top: 30px; height: 214px; width: 1px; background: var(--grey-light); }
  .card--dark .divider { background: #555; }

  .person { position: absolute; left: 272px; top: 40px; }
  .person__name { color: var(--orange); font-size: 15px; font-weight: 600; }
  .person__title { font-size: 11.5px; font-style: italic; margin-top: 2px; }

  .contacts { position: absolute; left: 272px; top: 110px; list-style: none; }
  .contacts li { display: flex; align-items: center; gap: 8px; font-size: 11.5px; height: 26px; }
  .contacts svg { width: 11px; height: 11px; flex: none; }

  .decor-field { position: absolute; left: 0; top: 0; width: 300px; height: 281px; }
  .card--light .decor-field {
    background: radial-gradient(ellipse 60% 55% at 38% 58%, rgba(242,138,30,.13), rgba(242,138,30,0) 100%);
  }
  .card--dark .decor-field {
    background: radial-gradient(ellipse 60% 55% at 38% 58%, rgba(190,100,25,.32), rgba(190,100,25,0) 100%);
  }

  .services { position: absolute; left: 272px; top: 58px; }
  .services__heading { color: var(--orange); font-size: 13px; font-weight: 600; margin-bottom: 12px; }
  .services__list { list-style: none; }
  .services__list li { font-size: 11px; line-height: 19.5px; }

  .label {
    position: absolute; width: 500px; text-align: center;
    font-family: "Marcellus SC", Georgia, serif; font-size: 23px;
    letter-spacing: 3px; color: var(--label);
  }
  .label--fa { left: 72px; top: 346px; }
  .label--fb { left: 629px; top: 346px; }
  .label--ba { left: 72px; top: 730px; }
  .label--bb { left: 629px; top: 730px; }
</style>
</head>
<body>

<section class="card card--light front-a">
  <svg class="edge" viewBox="0 0 500 281" aria-hidden="true">
    <path d="M440 0 H500 V281 H440 C475 200 478 80 440 0 Z" fill="var(--orange)"/>
    <path d="M430 0 C470 80 468 200 432 281" fill="none" stroke="var(--grey)" stroke-width="3"/>
    <path d="M420 0 C460 80 456 200 424 281" fill="none" stroke="var(--grey-light)" stroke-width="1.5"/>
  </svg>
  <div class="brand"><span class="brand__dot"></span><span class="brand__name">BRIGHTPATH STRATEGIC<br>Advisers F.Z.E</span></div>
  <div class="divider"></div>
  <div class="person"><p class="person__name">Khalid Yousef Nasser</p><p class="person__title">Founder &amp; CEO</p></div>
  <ul class="contacts">
    <li><svg viewBox="0 0 10 10"><path d="M5 0a3.5 3.5 0 0 0-3.5 3.5C1.5 6 5 10 5 10s3.5-4 3.5-6.5A3.5 3.5 0 0 0 5 0zm0 5a1.4 1.4 0 1 1 0-2.8A1.4 1.4 0 0 1 5 5z" fill="var(--orange)"/></svg>Corvana Trade Park</li>
    <li><svg viewBox="0 0 10 10"><path d="M2 0l2 2.5-1 1.2a6 6 0 0 0 3.3 3.3l1.2-1L10 8 8.5 10C4 10 0 6 0 1.5z" fill="var(--orange)"/></svg>00990 555014229</li>
    <li><svg viewBox="0 0 10 10"><rect x="0" y="2" width="10" height="6.5" fill="var(--orange)"/><path d="M0 2l5 3.5L10 2" fill="none" stroke="#fff" stroke-width="1"/></svg>info@bsa-qx.com</li>
    <li><svg viewBox="0 0 10 10"><circle cx="5" cy="5" r="4.3" fill="none" stroke="var(--orange)" stroke-width="1.3"/><path d="M.7 5h8.6M5 .7c-2.4 2.6-2.4 6 0 8.6M5 .7c2.4 2.6 2.4 6 0 8.6" fill="none" stroke="var(--orange)" stroke-width=".9"/></svg>www.bsa-qx.com</li>
  </ul>
</section>
<p class="label label--fa">Business Card Front A</p>

<section class="card card--dark front-b">
  <svg class="edge" viewBox="0 0 500 281" aria-hidden="true">
    <path d="M440 0 H500 V281 H440 C475 200 478 80 440 0 Z" fill="var(--orange)"/>
    <path d="M430 0 C470 80 468 200 432 281" fill="none" stroke="var(--grey)" stroke-width="3"/>
    <path d="M420 0 C460 80 456 200 424 281" fill="none" stroke="#5a5a5a" stroke-width="1.5"/>
  </svg>
  <div class="brand"><span class="brand__dot"></span><span class="brand__name">BRIGHTPATH STRATEGIC<br>Advisers F.Z.E</span></div>
  <div class="divider"></div>
  <div class="person"><p class="person__name">Khalid Yousef Nasser</p><p class="person__title">Founder &amp; CEO</p></div>
  <ul class="contacts">
    <li><svg viewBox="0 0 10 10"><path d="M5 0a3.5 3.5 0 0 0-3.5 3.5C1.5 6 5 10 5 10s3.5-4 3.5-6.5A3.5 3.5 0 0 0 5 0zm0 5a1.4 1.4 0 1 1 0-2.8A1.4 1.4 0 0 1 5 5z" fill="var(--orange)"/></svg>Corvana Trade Park</li>
    <li><svg viewBox="0 0 10 10"><path d="M2 0l2 2.5-1 1.2a6 6 0 0 0 3.3 3.3l1.2-1L10 8 8.5 10C4 10 0 6 0 1.5z" fill="var(--orange)"/></svg>00990 555014229</li>
    <li><svg viewBox="0 0 10 10"><rect x="0" y="2" width="10" height="6.5" fill="var(--orange)"/><path d="M0 2l5 3.5L10 2" fill="none" stroke="var(--card-dark)" stroke-width="1"/></svg>info@bsa-qx.com</li>
    <li><svg viewBox="0 0 10 10"><circle cx="5" cy="5" r="4.3" fill="none" stroke="var(--orange)" stroke-width="1.3"/><path d="M.7 5h8.6M5 .7c-2.4 2.6-2.4 6 0 8.6M5 .7c2.4 2.6 2.4 6 0 8.6" fill="none" stroke="var(--orange)" stroke-width=".9"/></svg>www.bsa-qx.com</li>
  </ul>
</section>
<p class="label label--fb">Business Card Front B</p>

<section class="card card--light back-a">
  <div class="decor-field" role="img" aria-label="Faint warm orange glow where a large faded brand decoration sits"></div>
  <div class="services">
    <p class="services__heading">Training &amp; Consultancy on:</p>
    <ul class="services__list">
      <li>QBXR Assessment &amp; Training</li>
      <li>Leadership Development &amp; Coaching</li>
      <li>Change Management</li>
      <li>Strategy Management</li>
      <li>Performance Management</li>
      <li>Quality &amp; Process Management</li>
      <li>TQM</li>
      <li>HR Development</li>
      <li>HR Procedures &amp; Regulation</li>
    </ul>
  </div>
</section>
<p class="label label--ba">Business Card Back A</p>

<section class="card card--dark back-b">
  <div class="decor-field" role="img" aria-label="Soft dark amber glow where a large faded brand decoration sits"></div>
  <div class="services">
    <p class="services__heading">Training &amp; Consultancy on:</p>
    <ul class="services__list">
      <li>QBXR Assessment &amp; Training</li>
      <li>Leadership Development &amp; Coaching</li>
      <li>Change Management</li>
      <li>Strategy Management</li>
      <li>Performance Management</li>
      <li>Quality &amp; Process Management</li>
      <li>TQM</li>
      <li>HR Development</li>
      <li>HR Procedures &amp; Regulation</li>
    </ul>
  </div>
</section>
<p class="label label--bb">Business Card Back B</p>

</body>
</html>
```